Flyer for a Unique Type of Tax Services

Please refer to the attached sample design for reference. Feel free to change the wording as needed. Here is the project brief:

Objective:
Objective of this flyer is to introduce our services which we are launching soon, which is new of a kind, to our potential customers i.e. online tax return preparation. By looking at the flyer we want our target audience to get convinced of our services and visit our website and register with us. They don’t have to pay anything to register.

Our Competitors:
Currently there are three main options available to get tax returns prepared. First is to buy tax software and get tax return prepared at own, this is the cheapest option. There are studies that suggest that people who are not well aware of tax laws there are chances they miss certain tax refunds by filing returns at their own and potentially lose money. Second option is to go to the local offices of nation-wide tax service companies like Pell & Varne and Morrow Tandy. They open offices only during tax season i.e. Jan through April but they are not available other part of the year and their association with the customers is temporary. Third option is to go to a CPA office which are the most expensive and very few people go for this option.

Weaknesses of the Current Options:
By self-preparing tax returns, there are chances that one can overlook certain tax laws that can provide additional tax credits and exemptions to people and overall they could have got a higher tax refund from the Govt. but they may miss it.
By going to other competitors during the peak time when tax returns are due, there are high chances that they don't have enough time to do research to ensure maximum refunds based on the exact circumstances of the individuals at the peak time as many people come to them during that time. Also they are not available after the tax season to provide them any answers to their questions or provide them tax planning tips to help them save tax in the next season.
By going to the CPA office, they charge a lot of fees and also for any tax advice later during the year, they will charge additional fees.

What we are offering:
We are offering a new option i.e. online tax return preparation through experts. We'll charge the fees competitive to what people are paying to local tax providers. But we will be different than our competitors as we'll be providing value added service if they got their returns prepared through us. Value added services we will be free of any additional cost for our customers who'll get tax return prepared through us.

Our Target Audience:
Our target audience is any person or couple who go to the tax service providers like Pell & Varne or Morrow Tandy to get their tax returns prepared.

How We are Different:
Here is the summary of the unique aspects of our business as compared to the competitors:
- Customers just pay us the price for preparing the annual return and price is comparable and competitive to what they have been paying to other providers.
- Unlike our competitors, we do extensive research to review the circumstances of our customers and explore applicable tax laws to make sure all available tax credits, exemptions, and deductions are taken for our customers, whereas our customers don't usually do such kind of research as during the peak tax season when customers approach them they usually don’t have time to do that kind of research. We start our association with our customers much sooner than the actual due date and this provides us time to do extensive research and we try our best that our customers could get higher tax returns.
- By just getting tax returns prepared through us, we enter into a long-term association with our customers and provide them complimentary tax planning tips throughout the year to help them save tax in the following year
- We are available to our customers year-round to provide complementary answers to any tax related questions without any additional cost e.g. how to save tax when buying a car, whether to buy or lease the care to save tax, for the sole-proprietor business how to save tax by using portion of the home as home-office, how to save tax by using personal car for personal business.
- We also provide answers to other basic financial advise related matters e.g. which insurance product is better, whether full insurance or term-life insurance to chose, how to save for the retirement etc.

Other Details:
Our logo has already been designed and we want the same logo to be used in the flyer. Our website address is: www.FiledRightPlus.com (it is still under construction but to get perspective of what we are trying to offer, visit this alternate website that it not final yet but will give an idea: http://www.filedrightplus.com/wordpress. Fyi, a video at this link is only a placeholder and not relevant to our services)

Requirements
Must have
• Please refer to the sample flyer attached. Feel free to change the design and language.
Should not have
• Please do not put any testimonial on the flyer as reflected in the under construction website.

```html
<!DOCTYPE html>
<html lang="en">
<head>
<meta charset="utf-8">
<title>Filed Right Plus – Flyer</title>
<link rel="stylesheet" href="https://fonts.googleapis.com/css2?family=Cinzel:wght@400;600&family=Roboto+Condensed:wght@300;400;700&display=swap">
<style>
  :root {
    --stage: #5b5e64;
    --blue-light: #3d74e6;
    --blue-deep: #2c50c0;
    --bubble: #f07025;
    --bubble-shadow: #1d3684;
    --figure-top: #0c0f1a;
    --figure-bottom: #1a2a63;
    --white: #ffffff;
    --ink-grey: #55595f;
    --accent-orange: #f07025;
    --brand-blue: #1f3fa6;
    --rule: rgba(255,255,255,0.25);
  }
  * { box-sizing: border-box; margin: 0; padding: 0; }
  html, body {
    width: 1200px; height: 1000px; overflow: hidden;
    background: var(--stage);
  }
  .flyer {
    position: absolute;
    left: 293px; top: 22px;
    width: 614px; height: 950px;
    background: radial-gradient(ellipse at 50% 40%, var(--blue-light) 0%, var(--blue-deep) 75%);
    box-shadow: 0 6px 24px rgba(0,0,0,0.45);
    overflow: hidden;
    font-family: "Roboto Condensed", "Arial Narrow", sans-serif;
  }
  .figure-art {
    position: absolute;
    left: 169px; top: 108px;
    width: 266px; height: 490px;
    border-radius: 60px 60px 10px 10px;
    background: linear-gradient(180deg, var(--figure-top) 0%, var(--figure-top) 72%, var(--figure-bottom) 100%);
    opacity: 0.9;
  }
  .bubble { position: absolute; }
  .bubble svg { position: absolute; left: 0; top: 0; overflow: visible; }
  .bubble .bubble-fill { fill: var(--bubble); }
  .bubble .bubble-shade { fill: var(--bubble-shadow); opacity: 0.8; }
  .bubble p {
    position: relative;
    color: var(--white);
    font-weight: 300;
    font-size: 13.5px;
    line-height: 19px;
  }
  .bubble strong { font-weight: 700; }

  .bubble--research { left: 176px; top: 64px; width: 332px; height: 52px; }
  .bubble--research p { padding: 6px 10px 0 9px; }
  .bubble--advice { left: 49px; top: 196px; width: 223px; height: 66px; }
  .bubble--advice p { padding: 7px 8px 0 8px; text-align: right; }
  .bubble--tips { left: 324px; top: 371px; width: 236px; height: 85px; }
  .bubble--tips p { padding: 6px 8px 0 9px; }

  .pitch {
    position: absolute; left: 0; top: 626px; width: 614px;
    text-align: center; color: var(--white);
    font-family: "Cinzel", "Trajan Pro", serif;
  }
  .pitch-lead { font-size: 21px; line-height: 23px; font-weight: 600; }
  .pitch-hook { font-size: 36px; line-height: 44px; margin-top: 2px; font-weight: 400; }
  .rule {
    position: absolute; left: 48px; top: 748px; width: 518px; height: 1px;
    background: linear-gradient(90deg, transparent, var(--rule), transparent);
  }
  .pitch-detail {
    position: absolute; left: 60px; top: 758px; width: 494px;
    text-align: center; color: var(--white);
    font-size: 10.5px; line-height: 15px; font-weight: 300;
  }
  .footer {
    position: absolute; left: 0; bottom: 0; width: 614px; height: 142px;
    background: var(--white);
  }
  .register {
    position: absolute; left: 40px; top: 44px;
    color: var(--ink-grey);
  }
  .register-lead { font-size: 22px; font-weight: 300; line-height: 24px; }
  .register-url { font-size: 27px; font-weight: 300; line-height: 30px; }
  .register-url b { color: var(--accent-orange); font-weight: 700; }
  .brand {
    position: absolute; left: 350px; top: 50px;
    display: flex; align-items: center; gap: 10px;
    color: var(--brand-blue);
    font-size: 30px; font-weight: 700; letter-spacing: 0.5px;
  }
  .brand-dot {
    width: 22px; height: 22px; border-radius: 50%;
    background: var(--accent-orange);
  }
</style>
</head>
<body>
  <main class="flyer">
    <div class="figure-art" role="img" aria-label="Silhouette of a businessman in a suit dissolving into falling dollar signs"></div>

    <div class="bubble bubble--research">
      <svg width="332" height="62" aria-hidden="true">
        <path class="bubble-shade" d="M-8 8 H324 V70 L310 60 H-8 Z"/>
        <path class="bubble-fill" d="M0 0 H332 V62 L318 52 H0 Z"/>
      </svg>
      <p>Does your Tax Return Preparer have time to do <strong>Extensive Research</strong> for you to help you get <strong>maximum refunds</strong>?</p>
    </div>

    <div class="bubble bubble--advice">
      <svg width="223" height="81" aria-hidden="true">
        <path class="bubble-shade" d="M-6 6 H217 V72 H8 L-6 87 Z"/>
        <path class="bubble-fill" d="M0 0 H223 V66 H14 L0 81 Z"/>
      </svg>
      <p>Do you get year-round <strong>Free Advice</strong> regarding your <strong>Tax related Questions</strong> from your exiting Tax Service Provider</p>
    </div>

    <div class="bubble bubble--tips">
      <svg width="236" height="99" aria-hidden="true">
        <path class="bubble-shade" d="M6 7 H242 V106 L226 92 H6 Z"/>
        <path class="bubble-fill" d="M0 0 H236 V99 L220 85 H0 Z"/>
      </svg>
      <p>Does your existing Tax Service Provider give you <strong>Complementary Tax Planning Tips</strong> throughout the year to help you <strong>save tax in the following year</strong>?</p>
    </div>

    <section class="pitch">
      <p class="pitch-lead">If not, then try us as we do provide all these<br>services year-round to our customers who get tax<br>returns prepared through us at</p>
      <p class="pitch-hook">NO ADDITIONAL COST.</p>
    </section>
    <div class="rule"></div>
    <p class="pitch-detail">Right away we'll start doing research for you and will be available year-round to answer your tax related questions and we will keep providing you tax planning tips and also provide you guidelines on other financial planning matters.</p>

    <footer class="footer">
      <div class="register">
        <p class="register-lead">Register for FREE at</p>
        <p class="register-url"><b>FiledRightPlus</b>.com</p>
      </div>
      <div class="brand">
        <span class="brand-dot" aria-hidden="true"></span>
        <span class="brand-name">Filed Right Plus</span>
      </div>
    </footer>
  </main>
</body>
</html>
```